Velora Aesthetica

Medical doctor providing aesthetic medicine

* Double sided card
* Logo to be on card
Other details:
* Dr. Mirela Kostvan, BSc, MBChB, CCFP
* #214-215, 27903 83 Ave, Surrey, BC, V2T 4K7
* 604-718-2943
* info@veloraclinic.ca
* www.veloraclinic.ca

Industry/Entity Type

Medical / Health & Beauty

Contact Information for Business Card

see 'Project Description'

Colors
0054AA
0677BA
7BADD7
CADEEF
E8F1F8
FFF300
FFF600
FEFA6F
FFFEC7
FFFEE8

Requirements
Must have
• Modern, high-end design

```html
<!DOCTYPE html>
<html lang="en">
<head>
<meta charset="utf-8">
<title>Velora Aesthetica – Business Card</title>
<link rel="stylesheet" href="https://fonts.googleapis.com/css2?family=Montserrat:wght@400;500;600&display=swap">
<style>
  :root {
    --stage: #2b2d31;
    --navy: #1f3d62;
    --navy-deep: #1a3556;
    --navy-light: #2f5583;
    --gold: #d8ad2a;
    --soft-text: #c9d1dc;
    --white: #ffffff;
    --ink: #1c2430;
  }
  * { box-sizing: border-box; margin: 0; padding: 0; }
  html, body {
    width: 1200px; height: 900px; overflow: hidden;
    background: var(--stage);
    font-family: "Montserrat", sans-serif;
  }
  .canvas { position: relative; width: 1200px; height: 900px; }
  .card {
    position: absolute; left: 300px;
    width: 600px; height: 343px;
    background: var(--navy);
    border-radius: 4px;
    overflow: hidden;
    box-shadow: 0 14px 30px rgba(0,0,0,.45);
  }
  .card--front { top: 84px; }
  .card--back { top: 473px; background: var(--navy-deep); }

  .front-curve { position: absolute; inset: 0; width: 600px; height: 343px; }

  .contact { position: absolute; left: 40px; top: 38px; color: var(--soft-text); }
  .contact__name { color: var(--gold); font-weight: 600; font-size: 21px; letter-spacing: .2px; }
  .contact__credentials { font-size: 11px; margin-top: 4px; letter-spacing: .3px; }
  .contact__address { font-size: 11.5px; line-height: 1.55; margin-top: 30px; }
  .contact__list { list-style: none; margin-top: 20px; font-size: 11.5px; }
  .contact__list li { display: flex; align-items: center; gap: 9px; margin-bottom: 8px; }
  .contact__icon { width: 12px; height: 12px; flex: none; }

  .brand-name {
    position: absolute;
    font-weight: 500;
    text-transform: uppercase;
    white-space: nowrap;
    text-align: center;
  }
  .card--front .brand-name {
    left: 345px; width: 235px; top: 218px;
    font-size: 13px; letter-spacing: 3px; color: var(--ink);
  }
  .card--back .brand-name {
    left: 0; right: 0; top: 158px;
    font-size: 24px; letter-spacing: 6px; color: var(--navy-light);
  }
</style>
</head>
<body>
<main class="canvas">
  <section class="card card--front" aria-label="Card front">
    <svg class="front-curve" viewBox="0 0 600 343" aria-hidden="true">
      <path d="M318 343 C 290 210, 390 112, 600 104 L600 343 Z" fill="var(--white)"/>
      <path d="M330 320 C 312 205, 400 128, 560 116" fill="none" stroke="var(--gold)" stroke-width="2"/>
    </svg>

    <div class="contact">
      <h1 class="contact__name">Dr. Mirela Kostvan</h1>
      <p class="contact__credentials">BSc, MBChB, CCFP</p>
      <p class="contact__address">#214-215, 27903 83 Ave,<br>Surrey, BC, V2T 4K7</p>
      <ul class="contact__list">
        <li>
          <svg class="contact__icon" viewBox="0 0 12 12" aria-hidden="true"><path d="M2.5 1h2l1 2.7-1.3.9a6 6 0 0 0 3.2 3.2l.9-1.3 2.7 1v2a1 1 0 0 1-1 1A9.5 9.5 0 0 1 1.5 2a1 1 0 0 1 1-1z" fill="var(--gold)"/></svg>
          604-718-2943
        </li>
        <li>
          <svg class="contact__icon" viewBox="0 0 12 12" aria-hidden="true"><rect x="1" y="2.5" width="10" height="7" rx="1" fill="var(--gold)"/><path d="M1.5 3.2 6 6.6l4.5-3.4" fill="none" stroke="var(--navy)" stroke-width="1"/></svg>
          info@veloraclinic.ca
        </li>
        <li>
          <svg class="contact__icon" viewBox="0 0 12 12" aria-hidden="true"><circle cx="6" cy="6" r="5" fill="none" stroke="var(--gold)" stroke-width="1.2"/><ellipse cx="6" cy="6" rx="2" ry="5" fill="none" stroke="var(--gold)" stroke-width="1"/><path d="M1 6h10" stroke="var(--gold)" stroke-width="1"/></svg>
          www.veloraclinic.ca
        </li>
      </ul>
    </div>

    <p class="brand-name">Velora Aesthetica</p>
  </section>

  <section class="card card--back" aria-label="Card back">
    <p class="brand-name">Velora Aesthetica</p>
  </section>
</main>
</body>
</html>
```